International oil and gas consultancy business needs a web design

Hello, I need a web design for a new oil and gas auditing consultancy business. My business undertakes contract audit assignments to review past costs of oil and gas operations (see attached Excel file for more details of the businesses services). I need the design to give the impression of a professional consultancy style of business, rather than a retail style of website. Note: this job is for LAYOUT DESIGN ONLY and not coding / development work.
The following are my key design principles:
1. BASIC DESIGN: I am after a simple and static web design. I don't want the pages busy or cluttered with too many images or detail.
2. HORIZONTAL TABS: I require a horizontal set of tabs towards the top of the screens (see Excel file) which remain in the same position on every page.
3. META TAG PLANNING: The design should allow for effective positioning of content so that key meta tag words can easily be built during the technical build stage.
4. NUMBER OF PAGES: The site will eventually have a maximum of 10 pages. Seven of the pages will reside under the tabs. Can you please present your opening submission for the first two page.
5. USE OF MY LOGO: The attached logo (JPEG file) should be used throughout the website. Please don't change the shape and colour.
6. COLOUR SCHEMES: Can you please consider any of the 3 colour schemes below:
A - dark red (to match the logo), light grey and perhaps another of your liking;
B - dark red (to match the logo), light cream and perhaps another of your liking;
C - dark red (to match the logo), white and perhaps another of your liking.
7. WORD CONTENT: I have attached an Excel file which shows the estimated word content for each page.
8. FUTURE USE OF DESIGN: I'm planning on building a Wordpress website. Can you please ensure the layout design supports this application.

Target Market(s)

oil and gas companies (small and large)

Industry/Entity Type

Oil And Gas

Font styles to use
Sans Serif

Requirements
Nice to have
• The KOL logo and business name should ideally be next to each other. Also, the logo and name should be part of the background graphics, not above it.

```html
<!DOCTYPE html>
<html lang="en">
<head>
<meta charset="utf-8">
<title>KOL — Oil &amp; Gas Audit Consultancy</title>
<link href="https://fonts.googleapis.com/css2?family=Raleway:wght@400;500;600;700&display=swap" rel="stylesheet">
<style>
:root{
  --red:#8f1c1f;
  --red-dark:#7d1619;
  --pink:#e9cfd0;
  --ink:#333;
  --grey:#555;
  --muted:#999;
  --line:#bfbfbf;
  --white:#fff;
}
*{margin:0;padding:0;box-sizing:border-box}
html,body{width:1200px;height:912px;overflow:hidden;background:var(--white)}
body{font-family:'Raleway',sans-serif;color:var(--ink);position:relative}
.abs{position:absolute}
.brand{left:173px;top:22px;font-size:54px;font-weight:700;color:var(--red);letter-spacing:4px;line-height:60px}
.search{left:839px;top:22px;width:188px;height:21px;display:flex}
.search-field{flex:1;border:1px solid #888;font:400 10px 'Raleway',sans-serif;color:#aaa;padding:4px 6px;line-height:11px}
.search-btn{width:24px;background:var(--red)}
.nav{left:384px;top:77px;display:flex;gap:0;font-size:12.5px;font-weight:500;color:var(--ink)}
.nav a{color:inherit;text-decoration:none;position:absolute;top:0;white-space:nowrap}
.nav a.active{color:var(--red)}
.nav-underline{left:382px;top:97px;width:40px;height:5px;background:var(--red)}
.rule{left:170px;top:102px;width:858px;height:1px;background:var(--line)}
.hero-photo{left:170px;top:118px;width:576px;height:241px;background:linear-gradient(180deg,#8fa3c6 0%,#6a7fa4 22%,#3b4a66 45%,#4d5872 70%,#2d3a55 100%)}
.hero-panel{left:746px;top:118px;width:282px;height:241px;background:var(--red);color:var(--white);padding:17px 14px 0 18px}
.hero-panel h2{font-size:22.5px;font-weight:600;line-height:22px;letter-spacing:-.3px}
.hero-panel p{margin-top:10px;font-size:12.6px;line-height:16.7px;color:#f0d8d8}
.hero-btn{display:inline-block;margin-top:6px;margin-left:-2px;background:var(--white);color:var(--red);font-size:12.6px;padding:1px 11px 2px;text-decoration:none}
.welcome{left:171px;top:400px;width:530px}
.welcome h1{font-size:24px;font-weight:600;color:var(--red);line-height:28px}
.welcome .tagline{margin-top:3px;font-size:11.5px;color:var(--muted)}
.welcome .intro{margin-top:11px;font-size:12px;line-height:16.8px;color:var(--grey)}
.welcome .intro strong{color:var(--red);font-weight:600;font-size:14px}
.specialise{left:171px;top:545px;font-size:17.5px;font-weight:600;color:var(--grey);white-space:nowrap}
.service{width:170px;text-align:center;top:611px}
.service svg{display:block;margin:0 auto}
.service h3{margin-top:14px;font-size:14px;font-weight:700;color:var(--red)}
.service p{margin-top:6px;font-size:11px;line-height:14.5px;color:var(--grey)}
.divider{left:745px;top:400px;width:8px;height:390px;background:var(--pink)}
.sidebar{left:788px;top:400px;width:240px}
.sidebar h2{font-size:17.5px;font-weight:700;color:var(--red)}
.news{position:absolute;left:1px;width:240px}
.news h4{font-size:11.3px;font-weight:600;color:var(--grey)}
.news p{margin-top:3px;font-size:11px;line-height:14.5px;color:var(--grey)}
.news time{display:block;margin-top:4px;font-size:11px;color:var(--red)}
.newsletter-title{left:789px;top:675px;font-size:17.5px;font-weight:700;color:var(--red)}
.signup{left:791px;top:704px;width:188px;height:21px;display:flex}
.signup-field{flex:1;border:1px solid #888;font:400 12px 'Raleway',sans-serif;color:#aaa;padding:2px 7px}
.signup-btn{width:24px;background:var(--red);display:flex;align-items:center;justify-content:center}
.signup-note{left:792px;top:737px;width:220px;font-size:11px;line-height:14.5px;color:var(--grey)}
.footer-rule{left:170px;top:839px;width:858px;height:2px;background:linear-gradient(90deg,#ccc,#999 50%,#ccc)}
.footer-nav a{position:absolute;top:0;font-size:10.5px;color:var(--grey);text-decoration:none;white-space:nowrap}
.footer-nav{left:0;top:871px}
.copyright{right:175px;top:870px;font-size:10.5px;color:var(--ink)}
.copyright span{color:var(--red)}
</style>
</head>
<body>
<header>
  <div class="abs brand">KOL</div>
  <div class="abs search">
    <div class="search-field">Search here</div>
    <div class="search-btn"><svg width="24" height="21" viewBox="0 0 24 21"><circle cx="11" cy="9.5" r="4.5" fill="none" stroke="#fff" stroke-width="1.5"/><line x1="14.2" y1="12.8" x2="17.5" y2="16" stroke="#fff" stroke-width="1.8"/></svg></div>
  </div>
  <nav class="abs nav">
    <a class="active" style="left:0">HOME</a>
    <a style="left:61px">ABOUT US</a>
    <a style="left:149px">SERVICES</a>
    <a style="left:231px">OUR PARTNERS</a>
    <a style="left:350px">APPROACH</a>
    <a style="left:442px">WHY CHOSE US</a>
    <a style="left:562px">CONTACT US</a>
  </nav>
  <div class="abs nav-underline"></div>
  <div class="abs rule"></div>
</header>

<section>
  <div class="abs hero-photo" role="img" aria-label="Night view of an illuminated oil and gas processing plant"></div>
  <div class="abs hero-panel">
    <h2>Duis autem vel eum iriure dolor in hend</h2>
    <p>Lorem ipsum dolor sit amet, consectuer adipiscing elit, sed diam nionummy nibh euismod tincidunt ut laoreet dolore gna aliquam erat volutpat. Ut wisi em ad aim veniam, quis nostrud exerci tati mcorper suscipit lobortis nisl ut aliquip ex ea cndo consequat.</p>
    <a class="hero-btn">read more</a>
  </div>
</section>

<main>
  <div class="abs welcome">
    <h1>Welcome to our company</h1>
    <div class="tagline">We bring value, innovation and growth to your business</div>
    <p class="intro"><strong>Kestrel Oil Ledger Services</strong> is a Perth (Australia) based firm specialising in providing quality audit services for the oil and gas industry. Our skills and knowledge of oil and gas, along with a deep understanding of business commercial needs, ensures the high quality of our services</p>
  </div>
  <h2 class="abs specialise">Kestrel Oil Ledger Services specialise in the following services:</h2>

  <div class="abs service" style="left:155px">
    <svg width="76" height="76" viewBox="0 0 76 76"><circle cx="38" cy="38" r="36.5" fill="none" stroke="var(--red)" stroke-width="3"/><circle cx="38" cy="38" r="29" fill="var(--red)"/><rect x="25" y="28" width="20" height="22" rx="2" fill="none" stroke="#fff" stroke-width="2.5"/><path d="M34 41 L47 26 L51 30 L38 44 L33 45Z" fill="#fff"/></svg>
    <h3>Joint Venture adults</h3>
    <p>Lorem ipsum dolor sit amet, cectuer adipiscing</p>
  </div>
  <div class="abs service" style="left:349px">
    <svg width="76" height="76" viewBox="0 0 76 76"><circle cx="38" cy="38" r="36.5" fill="none" stroke="var(--red)" stroke-width="3"/><circle cx="38" cy="38" r="29" fill="var(--red)"/><rect x="28" y="23" width="21" height="29" rx="2" fill="none" stroke="#fff" stroke-width="2.5"/><g stroke="#fff" stroke-width="2"><line x1="25" y1="29" x2="30" y2="29"/><line x1="25" y1="35" x2="30" y2="35"/><line x1="25" y1="41" x2="30" y2="41"/><line x1="25" y1="47" x2="30" y2="47"/><line x1="34" y1="31" x2="44" y2="31"/></g></svg>
    <h3>Contract audits</h3>
    <p>Lorem ipsum dolor sit amet, cectuer adipiscing</p>
  </div>
  <div class="abs service" style="left:552px">
    <svg width="76" height="76" viewBox="0 0 76 76"><circle cx="38" cy="38" r="36.5" fill="none" stroke="var(--red)" stroke-width="3"/><circle cx="38" cy="38" r="29" fill="var(--red)"/><g fill="none" stroke="#fff" stroke-width="2.3"><rect x="26" y="38" width="6" height="10"/><rect x="35" y="32" width="6" height="16"/><rect x="44" y="25" width="6" height="23"/><line x1="23" y1="51" x2="53" y2="51"/></g></svg>
    <h3>Operation audits</h3>
    <p>Lorem ipsum dolor sit amet, cectuer adipiscing</p>
  </div>
</main>

<aside>
  <div class="abs divider"></div>
  <div class="abs sidebar">
    <h2>Latest News</h2>
    <article class="news" style="top:32px"><h4>Our Company organise adults for...</h4><p>Lorem ipsum dolor sit amet, cectuer adipiscing elit, sed diam nionummy nibh euismod</p><time>15 August 2014</time></article>
    <article class="news" style="top:113px"><h4>Our Company organise adults for...</h4><p>Lorem ipsum dolor sit amet, cectuer adipiscing elit, sed diam nionummy nibh euismod</p><time>15 August 2014</time></article>
    <article class="news" style="top:194px"><h4>Our Company organise adults for...</h4><p>Lorem ipsum dolor sit amet, cectuer adipiscing elit, sed diam nionummy nibh euismod</p><time>15 August 2014</time></article>
  </div>
  <h2 class="abs newsletter-title">Sign up for newsletter</h2>
  <div class="abs signup">
    <div class="signup-field">Your email address</div>
    <div class="signup-btn"><svg width="16" height="12" viewBox="0 0 16 12"><path d="M1 4H8V0.5L15 6L8 11.5V8H1Z" fill="#fff"/></svg></div>
  </div>
  <p class="abs signup-note">We will keep you up to date with news, events and other great features</p>
</aside>

<footer>
  <div class="abs footer-rule"></div>
  <nav class="abs footer-nav">
    <a style="left:171px">HOME</a>
    <a style="left:218px">ABOUT US</a>
    <a style="left:286px">SERVICES</a>
    <a style="left:350px">OUR PARTNERS</a>
    <a style="left:443px">APPROACH</a>
    <a style="left:514px">WHY CHOSE US</a>
    <a style="left:609px">CONTACT US</a>
  </nav>
  <div class="abs copyright">© 2014 <span>KOL</span>. All rights reserved</div>
</footer>
</body>
</html>
```